PolaPola - Syrup Corner: New bottle design

Hi there,
Hope you are doing fine during this challenging times. Our PolaPola-Syrup Corner is growing and we want to have a refresh of our bottle design.

see also our website: www.polapola.fizz

Logo Text

refer to briefing sheet and photos attached

Font styles to use
Other font styles liked:
• Shadeera

Requirements
Must have
• include the PolaPola Logo - we are open to any other design variants or ideas

```html
<!DOCTYPE html>
<html lang="de">
<head>
<meta charset="utf-8">
<title>PolaPola - Syrup Corner · Holunder Label</title>
<link href="https://fonts.googleapis.com/css2?family=Open+Sans:wght@400;600&family=Oswald:wght@500&display=swap" rel="stylesheet">
<style>
  :root {
    --label-black: #000000;
    --frost: #a9c4d6;
    --frame-grey: #8e9aa3;
    --orange: #f28a1d;
    --white: #ffffff;
    --page: #ffffff;
  }
  html, body {
    margin: 0;
    padding: 0;
    width: 1200px;
    height: 671px;
    overflow: hidden;
    background: var(--page);
  }
  .label {
    position: relative;
    width: 1200px;
    height: 671px;
    font-family: "Open Sans", sans-serif;
    color: var(--white);
  }
  .label-shape {
    position: absolute;
    inset: 0;
  }
  .volume {
    position: absolute;
    top: 236px;
    font-size: 19px;
    transform: translateX(-50%);
  }
  .volume--left { left: 302px; }
  .volume--right { left: 896px; }

  .brand {
    position: absolute;
    left: 600px;
    top: 305px;
    transform: translateX(-50%);
    display: flex;
    align-items: center;
    gap: 14px;
  }
  .brand-dot {
    width: 26px;
    height: 26px;
    border-radius: 50%;
    background: var(--frost);
  }
  .brand-name {
    font-size: 64px;
    font-weight: 600;
    color: var(--frost);
    letter-spacing: 1px;
    line-height: 1;
  }

  .date-grid {
    position: absolute;
    left: 32px;
    top: 227px;
    width: 25px;
    display: flex;
    flex-direction: column;
    align-items: center;
  }
  .date-grid__heading {
    font-family: "Oswald", sans-serif;
    font-size: 9px;
    line-height: 12px;
    letter-spacing: -0.2px;
  }
  .date-grid__heading--year { margin-top: 4px; }
  .date-grid__cell {
    width: 24px;
    height: 21px;
    margin-top: 3.4px;
    background: var(--orange);
    font-size: 15px;
    line-height: 21px;
    text-align: center;
  }

  .vertical {
    position: absolute;
    bottom: 45px;
    writing-mode: vertical-rl;
    transform: rotate(180deg);
    font-size: 19px;
    line-height: 1;
    white-space: nowrap;
  }
  .best-before { left: 74px; }
  .ingredients-title { left: 1023px; }
  .ingredients-list { left: 1051px; }
  .storage { left: 1080px; }
  .website { left: 1137px; }

  .flavour-row {
    position: absolute;
    top: 521px;
    left: 0;
    width: 1200px;
    font-size: 31px;
    line-height: 1;
  }
  .flavour-row span {
    position: absolute;
    transform: translateX(-50%);
  }
  .code--left { left: 385px; }
  .flavour-name { left: 597px; }
  .code--right { left: 825px; }

  .flavour-rule {
    position: absolute;
    left: 300px;
    top: 574px;
    width: 595px;
    height: 7px;
    background: var(--frost);
  }
  .claim {
    position: absolute;
    left: 600px;
    top: 609px;
    transform: translateX(-50%);
    font-size: 18.5px;
    white-space: nowrap;
  }
</style>
</head>
<body>
<main class="label">
  <svg class="label-shape" width="1200" height="671" viewBox="0 0 1200 671" aria-hidden="true">
    <path d="M0,195 H341 A268,268 0 0 1 857,195 H1200 V671 H0 Z" fill="var(--label-black)"/>
    <rect x="5" y="199" width="1190" height="467" fill="none" stroke="var(--frame-grey)" stroke-width="3"/>
    <rect x="10" y="204" width="1180" height="457" fill="none" stroke="var(--frame-grey)" stroke-width="1"/>
  </svg>

  <div class="volume volume--left">20 cl</div>
  <div class="volume volume--right">20 cl</div>

  <div class="brand">
    <span class="brand-dot"></span>
    <span class="brand-name">PolaPola</span>
  </div>

  <div class="date-grid">
    <span class="date-grid__heading">MONTH</span>
    <span class="date-grid__cell">1</span>
    <span class="date-grid__cell">2</span>
    <span class="date-grid__cell">3</span>
    <span class="date-grid__cell">4</span>
    <span class="date-grid__cell">5</span>
    <span class="date-grid__cell">6</span>
    <span class="date-grid__cell">7</span>
    <span class="date-grid__cell">8</span>
    <span class="date-grid__cell">9</span>
    <span class="date-grid__cell">10</span>
    <span class="date-grid__cell">11</span>
    <span class="date-grid__cell">12</span>
    <span class="date-grid__heading date-grid__heading--year">YEAR</span>
    <span class="date-grid__cell">19</span>
    <span class="date-grid__cell">20</span>
    <span class="date-grid__cell">21</span>
    <span class="date-grid__cell">22</span>
  </div>

  <div class="vertical best-before">Mindestens haltbar bis/ Best before:</div>

  <div class="flavour-row">
    <span class="code--left">G01</span>
    <span class="flavour-name">HOLUNDER</span>
    <span class="code--right">G01</span>
  </div>
  <div class="flavour-rule"></div>
  <div class="claim">Ohne künstliche Farb - und Konservierungsstoffe</div>

  <div class="vertical ingredients-title">Inhaltsstoffe/ Ingredients:</div>
  <div class="vertical ingredients-list">Basilikum, Zitronen, Zucker, Wasser</div>
  <div class="vertical storage">Kühl lagern/ Once open keep cool</div>
  <div class="vertical website">www.polapola.fizz</div>
</main>
</body>
</html>
```